New automotive search style homepage

Looking for someone that can create a new homepage layout for my company. What we currently have is a little plain above the fold. We are an automotive technology company, where we take over the negotiation for customers, and perhaps we can have a design that appeals to that idea more. The current chat container is our only way to search currently, but would love to have a hybrid chat and manual search container, with the manual fields being make and model. This shouldn't have a toggle, but a seamless split view housing both features. You can see current design of our site at motorlane.net

Target Market(s)

Car buyers

Industry/Entity Type

Automotive

Number of Pages Required

1 page

Colors
0054AA
0677BA
7BADD7
CADEEF
E8F1F8

Requirements
Must have
• Above the fold is the most important

```html
<!DOCTYPE html>
<html lang="en">
<head>
<meta charset="utf-8">
<title>MotorLane – Homepage Concept</title>
<link href="https://fonts.googleapis.com/css2?family=Inter:wght@400;500;600;700;800&display=swap" rel="stylesheet">
<style>
:root{
  --navy:#043f81;
  --blue:#3091fc;
  --sky:#63bcfe;
  --ice:#cbe9ff;
  --white:#f0f0f0;
  --board:#d7dde8;
  --ink:#111827;
  --muted:#6b7280;
  --panel:#f5f6f8;
  --line:#e5e7eb;
  --brand:#0a6cf0;
}
*{box-sizing:border-box;margin:0;padding:0}
html,body{width:1200px;height:2761px;overflow:hidden}
body{background:var(--board);font-family:'Inter',sans-serif;color:var(--ink);position:relative}
.abs{position:absolute}

/* style guide */
.guide-logo{left:210px;top:90px;font-size:20px;font-weight:800;color:var(--brand)}
.guide-title{font-size:20px;font-weight:500;color:var(--navy)}
.guide-font{left:490px;top:129px;font-size:16px;color:var(--navy)}
.swatch{width:40px;height:40px;border-radius:50%;top:120px}
.swatch-label{top:167px;font-size:8px;color:#4b5563;width:50px;text-align:center}

/* site */
.site{left:229px;top:240px;width:661px;height:2225px;background:#fff;overflow:hidden}
.hero{left:0;top:0;width:661px;height:580px;background:linear-gradient(180deg,#0b2fb8 0%,#1246d6 30%,#2f7cf0 58%,#9ccaf8 80%,#ffffff 100%)}
.nav-logo{left:15px;top:12px;font-size:10px;font-weight:800;color:#fff}
.nav-link{top:14px;font-size:6px;color:#fff}
.login{left:593px;top:11px;width:40px;height:16px;border:1px solid rgba(255,255,255,.7);border-radius:3px;font-size:6px;color:#fff;text-align:center;line-height:14px}
.hero-title{left:0;width:661px;top:60px;text-align:center;font-size:36px;font-weight:700;color:#fff;letter-spacing:-.5px}
.hero-sub{left:0;width:661px;top:108px;text-align:center;font-size:7.5px;color:rgba(255,255,255,.9)}
.search-panel{left:110px;top:136px;width:446px;height:120px;border-radius:10px;background:rgba(255,255,255,.16);border:1px solid rgba(255,255,255,.35)}
.panel-label{font-size:6px;font-weight:600;color:#fff}
.ai-box{left:9px;top:22px;width:193px;height:89px;border-radius:6px;border:1px solid rgba(255,255,255,.45);background:rgba(255,255,255,.08);padding:9px;font-size:6px;color:#fff}
.round{width:12px;height:12px;border-radius:50%}
.divider{left:222px;width:1px;height:30px;background:rgba(255,255,255,.45)}
.or{left:216px;top:62px;font-size:6px;color:#fff}
.select{left:244px;width:193px;height:26px;border-radius:5px;border:1px solid rgba(255,255,255,.5);background:rgba(255,255,255,.12);padding:4px 7px;color:#fff}
.select small{display:block;font-size:4px;opacity:.7}
.select span{font-size:7px}
.select i{position:absolute;right:7px;top:9px;font-style:normal;font-size:7px}
.find-btn{left:244px;top:84px;width:193px;height:27px;border-radius:5px;background:#fff;color:var(--brand);font-size:7px;font-weight:600;text-align:center;line-height:27px}
.quick{left:0;width:661px;top:266px;text-align:center;font-size:5px;color:#fff}
.chip{display:inline-block;background:var(--brand);color:#fff;border-radius:8px;padding:2px 5px;margin-left:3px;font-weight:600}
.hero-card{background:#fff;border-radius:8px;box-shadow:0 10px 30px rgba(10,40,120,.18);padding:8px}
.photo{border-radius:6px;background:linear-gradient(160deg,#f3f4f6,#cfd4dc 60%,#9aa1ab)}
.sparkle{left:316px;top:417px;width:37px;height:37px;border-radius:8px;background:var(--brand);box-shadow:0 6px 18px rgba(10,108,240,.5)}

/* sections */
.h2{font-size:24px;font-weight:500;letter-spacing:-.3px}
.center{left:0;width:661px;text-align:center}
.step-num{font-size:50px;font-weight:300;color:transparent;-webkit-text-stroke:1px #c9ccd2;width:120px;text-align:center;line-height:1}
.step-label{font-size:10px;width:140px;text-align:center}
.step-icon{width:20px;height:20px}
.link{font-size:6.5px;color:var(--brand)}

.deal{width:169px;height:212px;border-radius:8px;background:#fff;border:1px solid #eef0f3;box-shadow:0 2px 8px rgba(0,0,0,.04)}
.deal .photo{position:absolute;left:4px;top:6px;width:161px;height:91px}
.bookmark{position:absolute;right:7px;top:9px;width:9px;height:9px;border-radius:2px;background:#fff;border:1px solid #ccc}
.tag{position:absolute;left:9px;top:107px;font-size:4px;background:#dbeafe;color:var(--brand);padding:1px 3px;border-radius:2px}
.deal-name{position:absolute;left:9px;top:116px;font-size:8px;font-weight:500}
.deal-trim{position:absolute;left:9px;top:128px;font-size:5px;color:var(--muted)}
.deal-price{position:absolute;left:9px;top:146px;font-size:13px;font-weight:600}
.deal-est{position:absolute;left:9px;top:164px;font-size:5px;color:var(--brand)}
.deal-miles{position:absolute;right:8px;top:155px;font-size:5px}
.deal-badge{position:absolute;left:9px;top:177px;font-size:3.5px;background:#dcfce7;color:#15803d;padding:2px 4px;border-radius:4px}
.deal-colors{position:absolute;left:9px;top:197px;font-size:4px;color:var(--muted)}
.dot{display:inline-block;width:4px;height:4px;border-radius:50%;margin-right:2px;vertical-align:middle}

.compare{width:215px;height:252px;background:var(--panel);border-radius:8px}
.compare-title{position:absolute;left:0;width:215px;top:20px;text-align:center;font-size:11px}
.pill{position:absolute;width:168px;height:20px;border-radius:4px;font-size:6.5px;line-height:20px;text-align:center}
.pill.old{background:#fff;color:#555;box-shadow:0 2px 6px rgba(0,0,0,.06)}
.pill.out{background:#fff;color:var(--brand);border:1px solid var(--brand)}
.pill.fill{background:var(--brand);color:#fff}

.faq-title{left:62px;top:1630px;font-size:26px;font-weight:500;line-height:30px;letter-spacing:-.3px}
.faq-box{left:328px;top:1628px;width:271px;height:107px;background:var(--panel);border-radius:8px}
.faq-row{position:absolute;left:10px;width:251px;height:26px;background:#fff;border-radius:4px;font-size:6.5px;padding:0 9px;line-height:26px}
.faq-row b{position:absolute;right:9px;font-weight:400;color:#888}

.cta{left:0;top:1796px;width:661px;height:429px;background:linear-gradient(180deg,#1a6df0 0%,#0a88e6 25%,#0a5ad8 50%,#0a2fa8 75%,#061466 100%)}
.cta-input{left:137px;top:89px;width:386px;height:40px;border-radius:8px;background:rgba(255,255,255,.2);border:1px solid rgba(255,255,255,.5);font-size:7px;color:#fff;padding:0 12px;line-height:38px}
.trust{top:147px;font-size:6px;color:#fff}
.f-head{font-size:6px;color:rgba(255,255,255,.6)}
.f-link{font-size:7.5px;color:#fff}
.small-white{font-size:5px;color:rgba(255,255,255,.8)}
.mega{left:66px;top:360px;font-size:110px;font-weight:800;color:#fff;letter-spacing:-2px;line-height:1}
</style>
</head>
<body>

<!-- style guide -->
<div class="abs guide-logo">MotorLane</div>
<div class="abs guide-title" style="left:489px;top:90px">Fonts:</div>
<div class="abs guide-font">Inter</div>
<div class="abs guide-title" style="left:685px;top:90px">Colors:</div>
<div class="abs swatch" style="left:685px;background:var(--navy)"></div>
<div class="abs swatch" style="left:731px;background:var(--blue)"></div>
<div class="abs swatch" style="left:777px;background:var(--sky)"></div>
<div class="abs swatch" style="left:823px;background:var(--ice)"></div>
<div class="abs swatch" style="left:869px;background:#fff"></div>
<div class="abs swatch-label" style="left:680px">#043f81</div>
<div class="abs swatch-label" style="left:726px">#3091fc</div>
<div class="abs swatch-label" style="left:772px">#63bcfe</div>
<div class="abs swatch-label" style="left:818px">#cbe9ff</div>
<div class="abs swatch-label" style="left:864px">#f0f0f0</div>

<main class="abs site">
  <!-- hero -->
  <section class="abs hero">
    <div class="abs nav-logo">MotorLane</div>
    <div class="abs nav-link" style="left:208px">Sell Your Car</div>
    <div class="abs nav-link" style="left:278px">Deals</div>
    <div class="abs nav-link" style="left:325px">Insurance</div>
    <div class="abs nav-link" style="left:385px">Research</div>
    <div class="abs nav-link" style="left:437px;color:var(--sky)">PRO</div>
    <svg class="abs" style="left:572px;top:15px" width="10" height="10" viewBox="0 0 10 10"><circle cx="4" cy="4" r="3" fill="none" stroke="#fff" stroke-width="1"/><path d="M6.3 6.3L9 9" stroke="#fff"/></svg>
    <div class="abs login">Login</div>
    <svg class="abs" style="left:641px;top:15px" width="10" height="9" viewBox="0 0 10 9"><path d="M0 1h10M0 4.5h10M0 8h10" stroke="#fff"/></svg>

    <h1 class="abs hero-title">Car Buying - Reversed</h1>
    <p class="abs hero-sub">Use AI search or browse by make and model. MotorLane experts negotiate the best price for you.</p>

    <div class="abs search-panel">
      <div class="abs panel-label" style="left:9px;top:10px">AI Search</div>
      <div class="abs ai-box">I want a used 2022 Kestrel Meridian in black... |
        <div class="abs round" style="left:156px;top:69px;background:rgba(255,255,255,.85)"></div>
        <div class="abs round" style="left:172px;top:69px;background:var(--brand)"></div>
      </div>
      <div class="abs divider" style="top:22px"></div>
      <div class="abs or">OR</div>
      <div class="abs divider" style="top:80px"></div>
      <div class="abs panel-label" style="left:244px;top:10px">Manual Search</div>
      <div class="abs select" style="top:23px"><small>MAKE</small><span>All Makes</span><i>⌄</i></div>
      <div class="abs select" style="top:54px"><small>MODEL</small><span>All Models</span><i>⌄</i></div>
      <div class="abs find-btn">Find Your Car ⌕</div>
    </div>
    <div class="abs quick">Quick search: <span class="chip">Kestrel Trailmark</span><span class="chip">Kestrel Solstra</span></div>

    <div class="abs hero-card" style="left:178px;top:320px;width:175px;height:215px;transform:rotate(-13deg)">
      <div class="photo" role="img" aria-label="Silver minivan photo" style="height:105px"></div>
      <div style="font-size:8px;margin-top:14px">Kestrel Trailmark</div>
      <div style="font-size:13px;font-weight:600;margin-top:18px">$23,500</div>
      <div style="font-size:5px;color:var(--brand)">Est. $350/mo*</div>
    </div>
    <div class="abs hero-card" style="left:355px;top:390px;width:130px;height:155px;transform:rotate(9deg)">
      <div class="photo" role="img" aria-label="Gray minivan photo" style="height:75px"></div>
      <div style="font-size:6.5px;margin-top:8px">Kestrel Solstra</div>
      <div style="font-size:10px;font-weight:600;margin-top:10px">$51,500</div>
      <div style="font-size:4.5px;color:var(--brand)">Est. $350/mo*</div>
    </div>
    <div class="abs hero-card" style="left:292px;top:336px;width:98px;height:34px;padding:4px;border-radius:5px">
      <div style="height:12px;border:1px solid var(--brand);border-radius:6px;font-size:3.5px;line-height:10px;padding-left:6px;color:#888">Refine — add "hybrid"</div>
      <div style="font-size:3.5px;text-align:center;margin-top:5px">Save search</div>
    </div>
    <div class="abs sparkle"><svg width="37" height="37" viewBox="0 0 37 37"><path d="M18.5 8 Q20 17 29 18.5 Q20 20 18.5 29 Q17 20 8 18.5 Q17 17 18.5 8Z" fill="#fff"/></svg></div>
  </section>

  <!-- how it works -->
  <h2 class="abs h2 center" style="top:604px">How MotorLane Works</h2>
  <p class="abs center" style="top:642px;font-size:8px;color:#444">Simple. Secure. Fast.</p>
  <div class="abs step-num" style="left:40px;top:697px">01</div>
  <div class="abs step-num" style="left:190px;top:683px">02</div>
  <div class="abs step-num" style="left:346px;top:683px">03</div>
  <div class="abs step-num" style="left:496px;top:697px">04</div>
  <svg class="abs step-icon" style="left:88px;top:754px" viewBox="0 0 20 20"><circle cx="8" cy="8" r="6" fill="none" stroke="var(--brand)" stroke-width="1.2"/><path d="M12.5 12.5L18 18" stroke="var(--brand)" stroke-width="1.2"/></svg>
  <svg class="abs step-icon" style="left:239px;top:740px" viewBox="0 0 20 20"><rect x="1" y="2" width="10" height="11" rx="1" fill="none" stroke="var(--brand)"/><circle cx="13" cy="13" r="5.5" fill="#fff" stroke="var(--brand)"/><text x="13" y="15.5" font-size="7" text-anchor="middle" fill="var(--brand)" font-family="Inter,sans-serif">$</text></svg>
  <svg class="abs step-icon" style="left:396px;top:740px" viewBox="0 0 20 20"><circle cx="10" cy="8" r="6.5" fill="none" stroke="var(--brand)"/><path d="M7 14l-1 5 4-2 4 2-1-5" fill="none" stroke="var(--brand)"/><text x="10" y="10.5" font-size="7" text-anchor="middle" fill="var(--brand)" font-family="Inter,sans-serif">$</text></svg>
  <svg class="abs step-icon" style="left:548px;top:754px" viewBox="0 0 20 20"><path d="M2 12l2-6h12l2 6v4H2z" fill="none" stroke="var(--brand)"/><circle cx="6" cy="16" r="1.8" fill="#fff" stroke="var(--brand)"/><circle cx="14" cy="16" r="1.8" fill="#fff" stroke="var(--brand)"/></svg>
  <div class="abs step-label" style="left:30px;top:786px">Find Your Car</div>
  <div class="abs step-label" style="left:179px;top:773px">Start AI Negotiations</div>
  <div class="abs step-label" style="left:336px;top:773px">Review Your Offers</div>
  <div class="abs step-label" style="left:486px;top:786px">Choose Your Deal</div>

  <!-- daily deals -->
  <h2 class="abs h2" style="left:62px;top:886px">Daily Deals</h2>
  <a class="abs link" style="left:534px;top:899px">Browse All Deals</a>

  <article class="abs deal" style="left:62px;top:938px">
    <div class="photo" role="img" aria-label="Silver minivan photo"></div><span class="bookmark"></span>
    <span class="tag">USED</span><div class="deal-name">Kestrel Trailmark</div><div class="deal-trim">LT</div>
    <div class="deal-price">$23,500</div><div class="deal-miles">◷ 16,134 mi</div><div class="deal-est">Est. $350/mo*</div>
    <div class="deal-badge">● 10 days on market</div>
    <div class="deal-colors"><span class="dot" style="background:#eee"></span>White &nbsp; <span class="dot" style="background:#555"></span>Gray</div>
  </article>
  <article class="abs deal" style="left:246px;top:938px">
    <div class="photo" role="img" aria-label="Gray minivan photo" style="background:linear-gradient(160deg,#f3f4f6,#a8adb5 60%,#6b7079)"></div><span class="bookmark"></span>
    <span class="tag">USED</span><div class="deal-name">Kestrel Solstra</div><div class="deal-trim">XLE</div>
    <div class="deal-price">$51,500</div><div class="deal-miles">◷ 16,134 mi</div><div class="deal-est">Est. $350/mo*</div>
    <div class="deal-badge">● 10 days on market</div>
    <div class="deal-colors"><span class="dot" style="background:#eee"></span>White &nbsp; <span class="dot" style="background:#555"></span>Gray</div>
  </article>
  <article class="abs deal" style="left:430px;top:938px">
    <div class="photo" role="img" aria-label="Dark gray cargo van photo" style="background:linear-gradient(160deg,#f3f4f6,#8c9199 55%,#4b5058)"></div><span class="bookmark"></span>
    <span class="tag">USED</span><div class="deal-name">Valtren Cargovan</div><div class="deal-trim">LT</div>
    <div class="deal-price">$23,500</div><div class="deal-miles">◷ 16,134 mi</div><div class="deal-est">Est. $350/mo*</div>
    <div class="deal-badge">● 10 days on market</div>
    <div class="deal-colors"><span class="dot" style="background:#eee"></span>White &nbsp; <span class="dot" style="background:#555"></span>Gray</div>
  </article>
  <article class="abs deal" style="left:614px;top:938px">
    <div class="photo" role="img" aria-label="Silver minivan photo"></div>
    <span class="tag">USED</span><div class="deal-name">Kestrel Trailmark</div><div class="deal-trim">LT</div>
    <div class="deal-price">$23,500</div><div class="deal-est">Est. $350/mo*</div>
    <div class="deal-badge">● 10 days on market</div>
    <div class="deal-colors"><span class="dot" style="background:#eee"></span>White &nbsp; <span class="dot" style="background:#555"></span>Gray</div>
  </article>

  <!-- old vs new -->
  <h2 class="abs h2 center" style="top:1234px">The Old Way vs The MotorLane Way</h2>
  <div class="abs compare" style="left:103px;top:1292px">
    <div class="compare-title">The Old Way</div>
    <div class="pill old" style="left:20px;top:50px;transform:rotate(-3deg)">You visit dealership after dealership</div>
    <div class="pill old" style="left:28px;top:82px;transform:rotate(2deg)">Every salesperson has an agenda</div>
    <div class="pill old" style="left:20px;top:114px;transform:rotate(-3deg)">Inconsistent pricing and hidden fees</div>
    <div class="pill old" style="left:28px;top:146px;transform:rotate(2deg)">Hours of back-and-forth negotiation</div>
    <div class="pill old" style="left:20px;top:178px;transform:rotate(-3deg)">You leave wondering if you got played</div>
    <div class="pill old" style="left:28px;top:210px;transform:rotate(2deg)">Pressure to decide on dealer's timeline</div>
  </div>
  <div class="abs compare" style="left:342px;top:1292px">
    <div class="compare-title" style="color:var(--brand);font-weight:600">The MotorLane Way</div>
    <div class="pill out" style="left:20px;top:50px;transform:rotate(3deg)">Dealers come to you</div>
    <div class="pill fill" style="left:30px;top:82px;transform:rotate(-3deg)">MotorLane works for buyers, not dealers</div>
    <div class="pill out" style="left:20px;top:114px;transform:rotate(3deg)">Transparent pricing from competing dealers</div>
    <div class="pill fill" style="left:30px;top:146px;transform:rotate(-3deg)">Built-in negotiation handles it</div>
    <div class="pill out" style="left:20px;top:178px;transform:rotate(3deg)">You leave knowing you got the best deal</div>
    <div class="pill fill" style="left:30px;top:210px;transform:rotate(-3deg)">Your timeline. Your decision</div>
  </div>

  <!-- faq -->
  <h2 class="abs faq-title">Got questions?<br>We have answers</h2>
  <p class="abs" style="left:62px;top:1696px;font-size:7px;color:#555">Everything you need to know before getting started.</p>
  <div class="abs faq-box">
    <div class="faq-row" style="top:10px">Does MotorLane cost anything to use?<b>+</b></div>
    <div class="faq-row" style="top:42px">Do I still have to negotiate with dealerships?<b>+</b></div>
    <div class="faq-row" style="top:72px">How do I know the price is fair?<b>+</b></div>
  </div>
  <a class="abs link" style="left:328px;top:1747px">View All Faqs</a>

  <!-- cta + footer -->
  <footer class="abs cta">
    <h2 class="abs h2 center" style="top:48px;color:#fff">Ready to find your next car?</h2>
    <div class="abs cta-input">I want a used 2022 Kestrel Meridian in black... |
      <div class="abs round" style="left:333px;top:13px;background:rgba(255,255,255,.5)"></div>
      <div class="abs round" style="left:352px;top:12px;width:15px;height:15px;background:#fff"></div>
    </div>
    <div class="abs trust" style="left:243px">✓ SSL Secured</div>
    <div class="abs trust" style="left:311px">✓ Top Rated</div>
    <div class="abs trust" style="left:371px">✓ Verified Dealers</div>
    <div class="abs" style="left:0;top:186px;width:661px;height:1px;background:rgba(255,255,255,.2)"></div>
    <div class="abs f-head" style="left:159px;top:219px">Company</div>
    <div class="abs f-link" style="left:159px;top:238px">About</div>
    <div class="abs f-link" style="left:159px;top:259px">Company</div>
    <div class="abs f-link" style="left:159px;top:280px">Affiliate Program</div>
    <div class="abs f-head" style="left:313px;top:219px">Resources</div>
    <div class="abs f-link" style="left:313px;top:238px">Guides</div>
    <div class="abs f-link" style="left:313px;top:259px">FAQs</div>
    <div class="abs f-head" style="left:439px;top:219px">For Buyers</div>
    <div class="abs f-link" style="left:439px;top:238px">Search</div>
    <div class="abs f-link" style="left:439px;top:259px">Daily Deals</div>
    <div class="abs f-link" style="left:439px;top:280px">How it Works</div>
    <div class="abs f-link" style="left:439px;top:301px">Car Value Calculator</div>
    <div class="abs small-white" style="left:66px;top:344px">© 2026 MotorLane. All rights reserved.</div>
    <div class="abs small-white" style="left:514px;top:344px">Terms &amp; Conditions | Privacy Policy</div>
    <div class="abs mega">MotorLane</div>
  </footer>
</main>
</body>
</html>
```